Briefbogen und Visitenkarte für Grundstücksverwaltunggesellschaft
Zielgruppe
Wir sind eine Grundstücksverwaltungsgesellschaft und Verwalten eine Vielzahl an Logistik- und Industrieimmobilien.
Aufgabenstellung
Wir bitten um Verwendung unseres Logo, siehe Anlage. Die Bildmarke darf nicht verändert werden, die Wortmarke darf unter Umständen otimiert werden.
Wir möchten einen dezenten Auftritt vermitteln und bitten daher um graue Schrift als Grundfarbe.
Bei der Visitenkarte könnten wir uns eine einfarbig blaue Rückseite vorstellen.
Folgende Daten kommen zur Verwendung:
Lindwerk Grundstücksverwaltungs GmbH
Internet: www.lindwerk-grundbesitz.de

```html
<!DOCTYPE html>
<html lang="de">
<head>
<meta charset="utf-8">
<title>Lindwerk Visitenkarte</title>
<link rel="stylesheet" href="https://fonts.googleapis.com/css2?family=Open+Sans:wght@400;600&display=swap">
<style>
  :root {
    --backdrop: #c6b29a;
    --brand-blue: #004f80;
    --paper: #f1f1f1;
    --band-light: #f2f2f2;
    --text-grey: #8a8a8a;
    --white: #ffffff;
  }
  html, body {
    margin: 0;
    width: 1200px;
    height: 1200px;
    overflow: hidden;
    background: var(--backdrop);
    font-family: "Open Sans", Arial, sans-serif;
  }
  .card {
    position: absolute;
    left: 224px;
    width: 719px;
    height: 463px;
    overflow: hidden;
  }
  .card--front { top: 116px; background: var(--brand-blue); }
  .card--back  { top: 650px; background: var(--paper); }

  .band { position: absolute; }
  .card--front .band { top: 209px; height: 52px; width: 137px; background: var(--band-light); }
  .band--left  { left: 0; }
  .band--right { right: 0; }

  .wordmark {
    position: absolute;
    display: flex;
    align-items: center;
    gap: 18px;
    font-weight: 600;
  }
  .wordmark__square { width: 40px; height: 40px; flex: none; }
  .wordmark__name { font-size: 30px; line-height: 1.1; letter-spacing: 1px; }
  .wordmark__legal { font-size: 15px; letter-spacing: 0.5px; line-height: 1.2; }

  .card--front .wordmark { left: 166px; top: 200px; color: var(--white); }
  .card--front .wordmark__square { background: var(--white); }

  .card--back .wordmark { left: 43px; top: 66px; color: var(--text-grey); }
  .card--back .wordmark__square { background: var(--text-grey); }

  .card--back .band--accent {
    right: 0; top: 82px; width: 263px; height: 51px; background: var(--brand-blue);
  }

  .contact {
    position: absolute;
    left: 174px;
    top: 162px;
    width: 400px;
    text-align: center;
    font-size: 15px;
    line-height: 20.5px;
    color: var(--text-grey);
  }
  .contact p { margin: 0 0 20px; }
  .contact .label { color: var(--brand-blue); }

  .role-band {
    position: absolute;
    left: 0; top: 371px;
    width: 461px; height: 52px;
    background: var(--brand-blue);
    color: var(--white);
    font-size: 23px;
    line-height: 52px;
    text-align: right;
    padding-right: 14px;
    box-sizing: border-box;
  }
  .person-name {
    position: absolute;
    left: 493px; top: 371px;
    line-height: 52px;
    font-size: 23px;
    color: var(--text-grey);
  }
</style>
</head>
<body>
  <section class="card card--front" aria-label="Vorderseite">
    <div class="band band--left"></div>
    <div class="band band--right"></div>
    <div class="wordmark">
      <span class="wordmark__square"></span>
      <div>
        <div class="wordmark__name">Lindwerk</div>
        <div class="wordmark__legal">Grundstücksverwaltungs GmbH</div>
      </div>
    </div>
  </section>

  <section class="card card--back" aria-label="Rückseite">
    <div class="wordmark">
      <span class="wordmark__square"></span>
      <div>
        <div class="wordmark__name">Lindwerk</div>
        <div class="wordmark__legal">Grundstücksverwaltungs GmbH</div>
      </div>
    </div>
    <div class="band band--accent"></div>

    <div class="contact">
      <p>Kornblumenweg 9<br>23562 Lübeck</p>
      <p>
        <span class="label">Telefon:</span> 0451 482760-0<br>
        <span class="label">Telefax:</span> 0451 482760-33<br>
        <span class="label">Mobil:</span> 0174 5523907 (nur auf VK)
      </p>
      <p>
        <span class="label">Internet:</span> www.lindwerk-grundbesitz.de<br>
        <span class="label">Mail:</span> info@lindwerk-grundbesitz.de
      </p>
    </div>

    <div class="role-band">Geschäftsführer</div>
    <div class="person-name">Jonas Berger</div>
  </section>
</body>
</html>
```